Business Card Design

I need a business card for my resume writing business. I have a logo that Im not keen on anymore so I would like the business card to use my photo instead of a logo. I am for mid career and trades resumes and prefer not to do executive resumes so don't need to aim for exectives. I would like it to be colourful. I like bright sky blue and maybe some pink or purple but primarily bright sky blue. I don't like green and Im keen see a fair bit of white on the card. As I have a photo to go it, it will need to go on a white background.

Target Market(s)

mid range careers. Not executives

Industry/Entity Type

Business

Contact Information for Business Card

Wyn Marchetti
Resume Writer
Clear Path CVs
27 The Lanyard
HARWOOD NSW 2465
wyn@clearpathcvs.com.au
0417362958
www.clearpathcvs.com.au

Requirements
Nice to have
• Maybe colours similar to my website - www.clearpathcvs.com.au but not with any black on it.
Should not have
• No green or dark colours

```html
<!DOCTYPE html>
<html lang="en">
<head>
<meta charset="utf-8">
<title>Wyn Marchetti – Business Card</title>
<link href="https://fonts.googleapis.com/css2?family=Arimo:wght@400&display=swap" rel="stylesheet">
<style>
  :root {
    --page: #ffffff;
    --card: #f4f9f7;
    --navy-blue: #0b5aa6;
    --sky-blue: #1a95d3;
    --sunshine: #f9b21b;
    --office-light: #eceeed;
    --office-mid: #dfe2e1;
    --hair-brown: #6e3f2e;
    --skin-warm: #d9a58c;
    --jacket-white: #f3f2ef;
    --jacket-shade: #e1ded9;
  }
  * { margin: 0; padding: 0; box-sizing: border-box; }
  html, body {
    width: 1200px;
    height: 369px;
    overflow: hidden;
    background: var(--page);
  }
  body {
    position: relative;
    font-family: "Arimo", Arial, sans-serif;
  }
  .card {
    position: absolute;
    top: 14px;
    width: 575px;
    height: 337px;
    background: var(--card);
    overflow: hidden;
  }
  .card--blue-rules { left: 18px; }
  .card--gold-rules { left: 608px; }

  .office-backdrop {
    position: absolute;
    left: 262px;
    top: 0;
    right: 0;
    height: 313px;
    background: linear-gradient(90deg, rgba(236,238,237,0) 0%, var(--office-light) 12%, var(--office-mid) 55%, var(--office-light) 100%);
  }

  .portrait {
    position: absolute;
    left: 315px;
    top: 12px;
    width: 260px;
    height: 301px;
    background: linear-gradient(180deg,
      var(--hair-brown) 0%,
      #8a5641 22%,
      var(--skin-warm) 40%,
      #e8d2c4 52%,
      var(--jacket-white) 64%,
      var(--jacket-shade) 82%,
      var(--jacket-white) 100%);
    -webkit-mask-image: linear-gradient(90deg, transparent 0%, #000 22%, #000 80%, transparent 100%);
            mask-image: linear-gradient(90deg, transparent 0%, #000 22%, #000 80%, transparent 100%);
  }

  .identity {
    position: absolute;
    right: 25px;
    top: 123px;
    text-align: right;
    color: var(--navy-blue);
    text-shadow: 0 0 6px rgba(255,255,255,0.8);
  }
  .identity__name {
    font-size: 19px;
    line-height: 22px;
  }
  .identity__role {
    font-size: 14px;
    line-height: 18px;
    color: var(--sky-blue);
  }

  .info-block {
    position: absolute;
    right: 316px;
    text-align: right;
    color: var(--sky-blue);
    font-size: 14px;
    line-height: 19px;
    padding-right: 7px;
  }
  .info-block::after {
    content: "";
    position: absolute;
    right: 0;
    top: 2px;
    bottom: 2px;
    width: 2px;
  }
  .card--blue-rules .info-block::after { background: var(--sky-blue); }
  .card--gold-rules .info-block::after { background: var(--sunshine); }

  .info-block--address { top: 165px; }
  .info-block--contact { top: 248px; }
  .info-block__company { color: var(--navy-blue); }

  .footer-band {
    position: absolute;
    left: 0;
    right: 0;
    top: 313px;
    height: 13px;
    display: flex;
  }
  .footer-band__gold { width: 262px; background: var(--sunshine); }
  .footer-band__blue { flex: 1; background: var(--navy-blue); }
</style>
</head>
<body>

  <div class="card card--blue-rules">
    <div class="office-backdrop"></div>
    <div class="portrait" role="img" aria-label="Portrait photo of the resume writer smiling, with shoulder-length brown hair and a white jacket, in a bright softly blurred office"></div>
    <div class="identity">
      <div class="identity__name">Wyn Marchetti</div>
      <div class="identity__role">Resume Writer</div>
    </div>
    <div class="info-block info-block--address">
      <div class="info-block__company">Clear Path CVs</div>
      <div>27 The Lanyard Harwood</div>
      <div>NSW 2465</div>
    </div>
    <div class="info-block info-block--contact">
      <div>wyn@clearpathcvs.com.au</div>
      <div>0417362958</div>
      <div>www.clearpathcvs.com.au</div>
    </div>
    <div class="footer-band">
      <div class="footer-band__gold"></div>
      <div class="footer-band__blue"></div>
    </div>
  </div>

  <div class="card card--gold-rules">
    <div class="office-backdrop"></div>
    <div class="portrait" role="img" aria-label="Portrait photo of the resume writer smiling, with shoulder-length brown hair and a white jacket, in a bright softly blurred office"></div>
    <div class="identity">
      <div class="identity__name">Wyn Marchetti</div>
      <div class="identity__role">Resume Writer</div>
    </div>
    <div class="info-block info-block--address">
      <div class="info-block__company">Clear Path CVs</div>
      <div>27 The Lanyard Harwood</div>
      <div>NSW 2465</div>
    </div>
    <div class="info-block info-block--contact">
      <div>wyn@clearpathcvs.com.au</div>
      <div>0417362958</div>
      <div>www.clearpathcvs.com.au</div>
    </div>
    <div class="footer-band">
      <div class="footer-band__gold"></div>
      <div class="footer-band__blue"></div>
    </div>
  </div>

</body>
</html>
```